Website for QuillbrookCrew presentation

We need a new website, ideally as a wordpress there, for QuillbrookCrew - we focus on machine learning, big data, data science and data analytics. This website should have two main sections - team presentation, introduction and offered services as static pages, and a blog section.

Target Market(s)

Companies which would like to hire the consultants for data science

Industry/Entity Type

Data Service

Font styles to use
Sans Serif

Colors

Designer to choose colors to be used in the design.

Requirements
Must have
• Wordpress template, blog and presentation pages, nice background images, incorporate the existing logo from brief
Nice to have
• match the word and ppt existing templates for quillbrook crew

```html
<!DOCTYPE html>
<html lang="en">
<head>
<meta charset="utf-8">
<title>QuillbrookCrew</title>
<link href="https://fonts.googleapis.com/css2?family=Montserrat:wght@400;600;700&family=Open+Sans:wght@400;600&display=swap" rel="stylesheet">
<style>
:root{
  --blue:#1e73be;
  --blue-dark:#1766ab;
  --svc1:#1b6db5;
  --svc2:#2378bf;
  --svc3:#2c84c7;
  --svc4:#3891cf;
  --navy:#061a2e;
  --ink:#222;
  --text:#333;
  --grey-bg:#f2f0f0;
  --footer:#5c5c5c;
  --white:#fff;
}
*{margin:0;padding:0;box-sizing:border-box}
html,body{width:1200px;height:3805px;overflow:hidden;background:var(--white)}
body{font-family:"Open Sans",Arial,sans-serif;color:var(--text);position:relative}
.abs{position:absolute}
.btn{position:absolute;display:inline-block;font-family:"Montserrat",Arial,sans-serif;font-weight:700;font-size:13px;padding:0 20px;line-height:30px;border-radius:2px;background:var(--blue);color:var(--white);text-decoration:none}
.btn.light{background:var(--white);color:var(--blue);font-size:11px;line-height:22px;padding:0 14px}
.btn.small{font-size:11px;line-height:24px;padding:0 16px}
h2.section-title{position:absolute;left:0;width:1200px;text-align:center;font-family:"Montserrat",Arial,sans-serif;font-weight:700;font-size:24px;color:var(--ink)}
.rule{position:absolute;left:572px;width:56px;height:3px;background:var(--blue)}

/* header */
.site-header{position:absolute;top:0;left:0;width:1200px;height:115px;background:var(--white);border-top:5px solid var(--blue)}
.brand{position:absolute;left:132px;top:26px;display:flex;align-items:center;gap:12px}
.brand-mark{width:44px;height:44px;border-radius:50%;background:var(--blue)}
.brand-name{font-family:"Montserrat",Arial,sans-serif;font-weight:700;font-size:20px;line-height:22px;color:var(--blue);width:150px}
.call{position:absolute;left:718px;top:26px;display:flex;gap:10px;align-items:center}
.call small{display:block;font-family:"Montserrat",Arial,sans-serif;font-weight:700;font-size:9px;color:var(--ink)}
.call strong{display:block;font-family:"Montserrat",Arial,sans-serif;font-weight:700;font-size:18px;color:var(--blue)}
.follow{position:absolute;left:910px;top:32px;display:flex;gap:6px;align-items:center;font-family:"Montserrat",Arial,sans-serif;font-weight:700;font-size:9px;color:var(--ink)}
.follow span.dot{width:20px;height:20px;border-radius:50%;background:var(--blue-dark)}
.follow span.label{margin-right:6px}
.nav{position:absolute;left:545px;top:79px;display:flex;gap:6px}
.nav a{font-family:"Montserrat",Arial,sans-serif;font-weight:700;font-size:12px;color:var(--ink);text-decoration:none;padding:3px 12px;border-radius:2px}
.nav a.active{background:var(--blue);color:var(--white)}

/* hero */
.hero{position:absolute;top:115px;left:0;width:1200px;height:588px;background:linear-gradient(90deg,#04101d 0%,#071d33 45%,#0a2c4c 100%);overflow:hidden}
.hero-art{position:absolute;left:620px;top:0;width:580px;height:588px;background:radial-gradient(ellipse at 55% 45%,#2a8fd0 0%,#125487 35%,rgba(7,29,51,0) 72%)}
.hero h1{position:absolute;left:198px;top:155px;font-family:"Montserrat",Arial,sans-serif;font-weight:700;font-size:68px;line-height:70px;color:var(--white)}
.hero p{position:absolute;left:198px;top:306px;width:330px;font-size:16px;line-height:20px;color:#e5eef7}
.hero .btn{left:198px;top:375px;line-height:34px;padding:0 22px;font-size:14px}
.dots{position:absolute;left:548px;top:528px;display:flex;gap:14px}
.dots i{width:8px;height:8px;border-radius:50%;background:#fff;display:block;opacity:.85}

/* welcome */
.welcome-art{position:absolute;left:162px;top:780px;width:362px;height:415px;background:radial-gradient(ellipse at 55% 40%,#d6e6f6 0%,#ffffff 75%)}
.welcome-kicker{position:absolute;left:627px;top:842px;font-family:"Montserrat",Arial,sans-serif;font-weight:700;font-size:22px;color:var(--ink)}
.welcome-title{position:absolute;left:627px;top:872px;font-family:"Montserrat",Arial,sans-serif;font-weight:700;font-size:34px;letter-spacing:1px;color:var(--blue)}
.welcome-copy{position:absolute;left:627px;top:942px;width:420px;font-size:12.5px;line-height:17px;color:var(--text)}
.welcome-copy p+p{margin-top:16px}
.welcome .btn{left:632px;top:1144px}

/* services */
.services{position:absolute;top:1268px;left:0;width:1200px;height:622px;display:flex}
.service{width:300px;height:622px;color:var(--white);text-align:center;position:relative}
.service:nth-child(1){background:var(--svc1)}
.service:nth-child(2){background:var(--svc2)}
.service:nth-child(3){background:var(--svc3)}
.service:nth-child(4){background:var(--svc4)}
.service svg{position:absolute;left:110px;top:200px}
.service h3{position:absolute;left:0;width:300px;top:338px;font-family:"Montserrat",Arial,sans-serif;font-weight:700;font-size:15px}
.service p{position:absolute;left:40px;width:220px;top:377px;font-size:11px;line-height:14px}
.service .btn{top:527px;left:50%;transform:translateX(-50%)}
.services-title{position:absolute;top:1335px;left:0;width:1200px;text-align:center;font-family:"Montserrat",Arial,sans-serif;font-weight:700;font-size:24px;color:var(--white)}
.services-rule{position:absolute;top:1380px;left:572px;width:56px;height:3px;background:var(--white)}

/* team */
.team{position:absolute;top:1890px;left:0;width:1200px;height:695px;background:var(--grey-bg)}
.member{position:absolute;top:212px;width:260px;text-align:center}
.avatar{width:164px;height:164px;margin:0 auto;border-radius:50%;border:10px solid #6b6b6b;background:linear-gradient(160deg,#8cc3e6 0%,#4f95c6 100%)}
.member h4{margin-top:34px;font-family:"Montserrat",Arial,sans-serif;font-weight:600;font-size:14px;color:var(--ink)}
.member p{margin:12px auto 0;width:230px;font-size:11px;line-height:14px;color:var(--text)}
.member .btn{position:relative;display:inline-block;margin-top:40px}
.arrow{position:absolute;top:372px;width:34px;height:34px;border-radius:50%;background:var(--white);box-shadow:0 1px 3px rgba(0,0,0,.15)}

/* blog */
.blog-card{position:absolute;top:2890px;width:255px;height:450px;background:var(--white)}
.blog-img{width:255px;height:235px;background:linear-gradient(135deg,#c9d6e3 0%,#7c9ebf 100%)}
.blog-card h4{margin:40px 0 0 22px;width:220px;font-family:"Montserrat",Arial,sans-serif;font-weight:700;font-size:14px;line-height:18px;color:var(--ink)}
.blog-card p{margin:12px 0 0 22px;width:200px;font-size:11.5px;line-height:15px;color:var(--text)}
.blog-card .btn{left:22px;top:398px}
.blog-divider{position:absolute;left:383px;top:2838px;width:1px;height:502px;background:#ddd}
.blog-feature{position:absolute;left:638px;top:2838px;width:562px;height:502px;background:radial-gradient(ellipse at 70% 45%,#1d6fc4 0%,#0d3a7a 50%,#071c3d 100%)}
.blog-feature h3{position:absolute;left:50px;top:140px;font-family:"Montserrat",Arial,sans-serif;font-weight:700;font-size:27px;line-height:32px;color:var(--white)}
.blog-feature p{position:absolute;left:50px;top:222px;width:230px;font-size:11px;line-height:14px;color:#dde8f5}
.blog-feature .btn{left:50px;top:315px}

/* footer */
.footer{position:absolute;top:3420px;left:0;width:1200px;height:385px;background:linear-gradient(180deg,#666 0%,#555 100%);color:var(--white)}
.footer-brand{position:absolute;left:150px;top:95px;display:flex;align-items:center;gap:16px}
.footer-brand .mark{width:60px;height:60px;border-radius:50%;background:var(--blue)}
.footer-brand .name{font-family:"Montserrat",Arial,sans-serif;font-weight:700;font-size:32px;line-height:34px;width:200px}
.fcol{position:absolute;top:70px;font-size:11px;line-height:14px}
.fcol h5{font-family:"Montserrat",Arial,sans-serif;font-weight:700;font-size:12px;margin-bottom:18px}
.fcol li{list-style:none}
.contact li{display:flex;gap:10px;align-items:flex-start;margin-bottom:16px}
.menu li{margin-bottom:1px}
.social li{display:flex;gap:10px;align-items:center;margin-bottom:15px}
.social li i{width:24px;height:24px;border-radius:50%;background:#1c3d6b;display:block}
.copyright{position:absolute;top:3764px;left:0;width:1200px;text-align:center;font-size:11px;color:#eee}
</style>
</head>
<body>

<header class="site-header">
  <div class="brand"><span class="brand-mark"></span><span class="brand-name">QUILLBROOK CREW</span></div>
  <div class="call">
    <svg width="22" height="22" viewBox="0 0 24 24"><path fill="#1e73be" d="M6.6 10.8a15 15 0 0 0 6.6 6.6l2.2-2.2c.3-.3.7-.4 1-.2 1.1.4 2.3.6 3.6.6.6 0 1 .4 1 1V20c0 .6-.4 1-1 1A17 17 0 0 1 3 4c0-.6.4-1 1-1h3.5c.6 0 1 .4 1 1 0 1.3.2 2.5.6 3.6.1.3 0 .7-.2 1z"/></svg>
    <div><small>CALL US</small><strong>555.014.2290</strong></div>
  </div>
  <div class="follow"><span class="label">FOLLOW US</span><span class="dot"></span><span class="dot"></span><span class="dot"></span></div>
  <nav class="nav">
    <a class="active" href="#">HOME</a><a href="#">ABOUT US</a><a href="#">SERVICES</a><a href="#">BLOG</a><a href="#">TEAM</a><a href="#">CONTACT US</a>
  </nav>
</header>

<section class="hero">
  <div class="hero-art" role="img" aria-label="Glowing blue circuit-board head in profile"></div>
  <h1>DATA<br>SCIENCE</h1>
  <p>But I must explain to you how all this mistaken idea of denouncing pleasure</p>
  <a class="btn" href="#">Read More</a>
  <div class="dots"><i></i><i></i><i></i><i></i><i></i></div>
</section>

<section class="welcome">
  <div class="welcome-art" role="img" aria-label="Line illustration of a head with a circuit-board brain"></div>
  <div class="welcome-kicker">WELCOME TO</div>
  <div class="welcome-title">QUILLBROOK CREW</div>
  <div class="welcome-copy">
    <p>On the other hand, we denounce with righteous indignation and dislike men who are so beguiled and demoralized by the charms of pleasure of the moment, so blinded by desire, that they cannot foresee the pain and trouble that are bound to ensue; and equal blame belongs to those who fail in their duty through weakness of will.</p>
    <p>So blinded by desire, that they cannot foresee the pain and trouble that are bound to ensue; and equal blame belongs to those who fail in their duty through weakness of will.</p>
  </div>
  <a class="btn" href="#">Read More</a>
</section>

<section class="services">
  <div class="service">
    <svg width="80" height="80" viewBox="0 0 80 80"><path fill="#fff" d="M40 8c-15 0-26 11-26 25 0 6 2 11 5 15v24h26v-9h8c3 0 5-2 5-5v-8l6-2-6-10C58 20 50 8 40 8z"/><g fill="#1b6db5"><rect x="28" y="30" width="4" height="12"/><rect x="35" y="24" width="4" height="18"/><rect x="42" y="28" width="4" height="14"/></g></svg>
    <h3>MACHINE LEARNING</h3>
    <p>On the other hand, we denounce with righteous indignation and dislike men who are so beguiled and demoralized by the charms of pleasure of the moment, so blinded by desire, that they cannot foresee the pain and trouble that are bound to ens accusamus et iusto.</p>
    <a class="btn light" href="#">Read More</a>
  </div>
  <div class="service">
    <svg width="80" height="80" viewBox="0 0 80 80" fill="none" stroke="#fff" stroke-width="3"><rect x="6" y="12" width="68" height="44" rx="2"/><path d="M32 56v10M48 56v10M24 68h32"/><path d="M14 44l14-14 10 8 12-16 14 10"/><circle cx="28" cy="30" r="2.5" fill="#fff"/><circle cx="38" cy="38" r="2.5" fill="#fff"/><circle cx="50" cy="22" r="2.5" fill="#fff"/></svg>
    <h3>BIG DATA</h3>
    <p>On the other hand, we denounce with righteous indignation and dislike men who are so beguiled and demoralized by the charms of pleasure of the moment, so blinded by desire, that they cannot foresee the pain and trouble that are bound to ens accusamus et iusto.</p>
    <a class="btn light" href="#">Read More</a>
  </div>
  <div class="service">
    <svg width="80" height="80" viewBox="0 0 80 80"><path fill="none" stroke="#fff" stroke-width="3" d="M32 8h16M34 8v22L16 62c-2 5 1 10 6 10h36c5 0 8-5 6-10L46 30V8"/><path fill="#fff" d="M24 52h32l6 11c1 3-1 5-4 5H22c-3 0-5-2-4-5z"/><circle cx="38" cy="20" r="2" fill="#fff"/><circle cx="43" cy="14" r="1.5" fill="#fff"/></svg>
    <h3>DATA SCIENCE</h3>
    <p>On the other hand, we denounce with righteous indignation and dislike men who are so beguiled and demoralized by the charms of pleasure of the moment, so blinded by desire, that they cannot foresee the pain and trouble that are bound to ens accusamus et iusto.</p>
    <a class="btn light" href="#">Read More</a>
  </div>
  <div class="service">
    <svg width="80" height="80" viewBox="0 0 80 80" fill="none" stroke="#fff" stroke-width="3"><path d="M6 72h68"/><rect x="12" y="50" width="10" height="20"/><rect x="28" y="42" width="10" height="28"/><rect x="44" y="46" width="10" height="24"/><rect x="60" y="30" width="10" height="40"/><path d="M14 34l16-12 14 8 20-18"/><circle cx="14" cy="34" r="3"/><circle cx="30" cy="22" r="3"/><circle cx="44" cy="30" r="3"/><circle cx="64" cy="12" r="3"/></svg>
    <h3>DATA ANALYTICS</h3>
    <p>On the other hand, we denounce with righteous indignation and dislike men who are so beguiled and demoralized by the charms of pleasure of the moment, so blinded by desire, that they cannot foresee the pain and trouble that are bound to ens accusamus et iusto.</p>
    <a class="btn light" href="#">Read More</a>
  </div>
</section>
<div class="services-title">OUR SERVICES</div>
<div class="services-rule"></div>

<section class="team">
  <h2 class="section-title" style="top:70px">OUR TEAM</h2>
  <div class="rule" style="top:115px"></div>
  <div class="arrow" style="left:80px"><svg width="34" height="34" viewBox="0 0 34 34"><path d="M19 12l-5 5 5 5" fill="none" stroke="#888" stroke-width="2"/></svg></div>
  <div class="arrow" style="left:1095px"><svg width="34" height="34" viewBox="0 0 34 34"><path d="M15 12l5 5-5 5" fill="none" stroke="#888" stroke-width="2"/></svg></div>
  <div class="member" style="left:175px">
    <div class="avatar" role="img" aria-label="Portrait photo of team member Marlow"></div>
    <h4>Marlow</h4>
    <p>On the other hand, we denounce with righteous indignation and dislike men who are so beguiled and demoralized by the charms of pleasure of the moment, so blinded by desire, which is the same as saying through shrinking from toil and pain</p>
    <a class="btn small" href="#">Read More</a>
  </div>
  <div class="member" style="left:470px">
    <div class="avatar" role="img" aria-label="Portrait photo of team member Teodor"></div>
    <h4>Teodor</h4>
    <p>On the other hand, we denounce with righteous indignation and dislike men who are so beguiled and demoralized by the charms of pleasure of the moment, so blinded by desire, which is the same as saying through shrinking from toil and pain</p>
    <a class="btn small" href="#">Read More</a>
  </div>
  <div class="member" style="left:788px">
    <div class="avatar" role="img" aria-label="Portrait photo of team member Ansel"></div>
    <h4>Ansel</h4>
    <p>On the other hand, we denounce with righteous indignation and dislike men who are so beguiled and demoralized by the charms of pleasure of the moment, so blinded by desire, which is the same as saying through shrinking from toil and pain</p>
    <a class="btn small" href="#">Read More</a>
  </div>
</section>

<section class="blog">
  <h2 class="section-title" style="top:2670px">LATEST BLOG</h2>
  <div class="rule" style="top:2717px"></div>
  <article class="blog-card" style="left:127px">
    <div class="blog-img" role="img" aria-label="Laptop showing data charts on a desk"></div>
    <h4>LOREM IPSUM DOLOR SIT SECTETUR ADIPISCI</h4>
    <p>Lorem ipsum dolor sit amet, consectetur adipiscing elit, sed do eiusmod tempor</p>
    <a class="btn small" href="#">Read More</a>
  </article>
  <div class="blog-divider"></div>
  <article class="blog-card" style="left:384px">
    <div class="blog-img" role="img" aria-label="Magnifying glass over a blue bar chart" style="background:linear-gradient(135deg,#bfe0f5 0%,#3f8fd0 100%)"></div>
    <h4>LOREM IPSUM DOLOR SIT SECTETUR ADIPISCI</h4>
    <p>Lorem ipsum dolor sit amet, consectetur adipiscing elit, sed do eiusmod tempor</p>
    <a class="btn small" href="#">Read More</a>
  </article>
  <article class="blog-feature" role="img" aria-label="Blue circuit board background">
    <h3>AT VERO EOS<br>ET ACCUSAMUS</h3>
    <p>On the other hand, we denounce with righteous indignation and dislike men who are so beguiled and demoralized by the charms of pleasure</p>
    <a class="btn small" href="#">Read More</a>
  </article>
</section>

<footer class="footer">
  <div class="footer-brand"><span class="mark"></span><span class="name">QUILLBROOK CREW</span></div>
  <div class="fcol contact" style="left:505px">
    <h5>CONTACT US</h5>
    <ul>
      <li><svg width="10" height="14" viewBox="0 0 10 14"><path fill="#fff" d="M5 0a5 5 0 0 0-5 5c0 4 5 9 5 9s5-5 5-9a5 5 0 0 0-5-5zm0 7a2 2 0 1 1 0-4 2 2 0 0 1 0 4z"/></svg><span>418 Larchmont Way<br>Fenwick, OR 97310</span></li>
      <li><svg width="12" height="12" viewBox="0 0 24 24"><path fill="#fff" d="M6.6 10.8a15 15 0 0 0 6.6 6.6l2.2-2.2c.3-.3.7-.4 1-.2 1.1.4 2.3.6 3.6.6.6 0 1 .4 1 1V20c0 .6-.4 1-1 1A17 17 0 0 1 3 4c0-.6.4-1 1-1h3.5c.6 0 1 .4 1 1 0 1.3.2 2.5.6 3.6.1.3 0 .7-.2 1z"/></svg><span>555.014.2290</span></li>
      <li><svg width="13" height="10" viewBox="0 0 13 10"><rect x=".5" y=".5" width="12" height="9" fill="none" stroke="#fff"/><path d="M.5 .5l6 5 6-5" fill="none" stroke="#fff"/></svg><span>info@quillbrookcrew.com</span></li>
    </ul>
  </div>
  <div class="fcol menu" style="left:755px">
    <h5>MENU</h5>
    <ul><li>Home</li><li>About Us</li><li>services</li><li>Blog</li><li>Team</li><li>Contact Us</li></ul>
  </div>
  <div class="fcol social" style="left:927px">
    <h5>CONNECT WITH US</h5>
    <ul><li><i></i>Chatterly</li><li><i></i>Birdcall</li><li><i></i>Linkwork</li></ul>
  </div>
</footer>
<div class="copyright">Copyright @ 2018 All Rights Reserved</div>

</body>
</html>
```